KORV LLP - Web Design - 20th Anniversary

Create a web page and secondary page for a law firm. The firm is an IP or Patent Law Firm, look should be cutting edge. They are looking for a tech feel high end look. They want some callout to note their anniversary. Blue needs to be more impactful then current site. - See Brief Colors will be Blue and Gold as they currently are. Would like to see a home page and an attorney bio page and something that calls out the anniversary

Target Market(s)

Tech and Patent Companies - See Brief

Industry/Entity Type

Legal

Number of Pages Required

2 page

Colors
0054AA
0677BA
7BADD7
CADEEF
E8F1F8
FFF300
FFF600
FEFA6F
FFFEC7
FFFEE8

Requirements
Must have
• Impactful Blue, Tech and Cutting Edge Feel - See Brief
Nice to have
• Something noting the Anniversary, but not the basic ribbon - See Brief
Should not have
• Do not use any regular law firm images court room, court steps gavel NO ON THESE

```html
<!DOCTYPE html>
<html lang="en">
<head>
<meta charset="utf-8">
<title>KORV LLP — Intellectual Property Law</title>
<link href="https://fonts.googleapis.com/css2?family=Roboto:wght@300;400;500;700;900&display=swap" rel="stylesheet">
<style>
:root{
  --blue:#0a50ae;
  --blue-deep:#0847a0;
  --blue-title:#0d57b8;
  --blue-light:#7badd7;
  --blue-pale:#cadeef;
  --nav:#5f92cf;
  --gold:#e6b414;
  --gold-light:#f6d24a;
  --orange:#f08a1c;
  --ink:#2b2b2b;
  --grey:#6f6f6f;
  --white:#ffffff;
}
*{margin:0;padding:0;box-sizing:border-box}
html,body{width:1200px;height:3160px;overflow:hidden}
body{position:relative;font-family:'Roboto',sans-serif;background:var(--white);color:var(--ink)}
.abs{position:absolute}

/* top bar & header */
.topbar{left:0;top:0;width:1200px;height:59px;background:var(--blue)}
.topbar .search{left:845px;top:14px}
.flag{top:17px;width:44px;height:25px;overflow:hidden}
.header{left:0;top:59px;width:1200px;height:101px;background:var(--white)}
.brand{left:117px;top:83px;display:flex;align-items:center;gap:14px}
.brand-mark{width:44px;height:44px;background:var(--blue);}
.brand-name{font-size:44px;font-weight:400;color:var(--blue-deep);letter-spacing:2px}
.nav a{position:absolute;top:99px;font-size:16px;font-weight:500;color:var(--nav);text-decoration:none;letter-spacing:.2px}
.nav a.active{color:var(--blue-deep)}
.nav a.active::after{content:"";position:absolute;left:50%;top:24px;width:5px;height:5px;margin-left:-2px;border-radius:50%;background:var(--orange)}

/* hero */
.hero{left:0;top:160px;width:1200px;height:549px;background:linear-gradient(120deg,#0a4ea9 0%,#0b57b6 60%,#0a4fa9 100%)}
.hero-title{left:134px;top:262px;font-size:52px;font-weight:900;line-height:60px;color:var(--white);letter-spacing:.5px}
.hero-sub{left:134px;top:514px;width:460px;font-size:16.5px;line-height:27px;color:var(--white)}
.badge{left:669px;top:196px;width:396px;height:393px;border-radius:50%;
  background:radial-gradient(circle at 50% 45%,var(--gold-light) 0%,var(--gold) 45%,rgba(230,180,20,.35) 62%,rgba(230,180,20,0) 72%)}
.badge-num{left:0;top:90px;width:100%;text-align:center;font-size:160px;font-weight:900;color:var(--white);line-height:1}
.badge-txt{left:0;top:246px;width:100%;text-align:center;font-size:46px;font-weight:900;color:var(--white)}

.stats{left:212px;top:628px;width:776px;height:151px;background:var(--white);border-radius:14px;box-shadow:0 3px 10px rgba(0,0,0,.18);display:flex}
.stat{flex:none;text-align:center;border-right:1px solid #e4e4e4;padding-top:36px}
.stat:last-child{border-right:none}
.stat b{display:block;font-size:36px;font-weight:500;color:var(--ink)}
.stat span{display:block;margin-top:14px;font-size:16.5px;color:var(--grey)}

/* services */
.sec-title{left:0;width:1200px;text-align:center;font-weight:700;color:var(--blue-title)}
.sec-sub{left:0;width:1200px;text-align:center;font-size:16.5px;line-height:22px;color:var(--ink)}
.card{top:979px;width:215px;height:196px;background:var(--white);border-radius:10px;box-shadow:0 2px 12px rgba(0,0,0,.09);text-align:center}
.card .ico{width:50px;height:50px;margin:25px auto 0;background:var(--blue);border-radius:6px;display:flex;align-items:center;justify-content:center}
.card h3{margin-top:22px;font-size:16px;font-weight:500;color:var(--ink)}
.card h3.two{margin-top:20px;font-size:12.5px;line-height:16px}
.card p{margin-top:12px;font-size:12.5px;line-height:21px;color:var(--grey);font-weight:300}
.card h3.two + p{margin-top:8px}
.arrow{top:1055px}

/* technologies */
.tech{left:135px;top:1227px;width:936px;height:687px;background:linear-gradient(160deg,#0b56b5,#0a4ea8);box-shadow:0 3px 8px rgba(0,0,0,.2)}
.tech h2{position:absolute;left:0;top:36px;width:100%;text-align:center;font-size:36px;font-weight:500;color:var(--white)}
.tech .lead{position:absolute;left:0;top:91px;width:100%;text-align:center;font-size:17px;color:var(--blue-pale)}
.ring{position:absolute;border-radius:50%;background:var(--blue-light);display:flex;align-items:center;justify-content:center}
.ring .photo{border-radius:50%;border:4px solid var(--blue-deep)}
.tlabel{position:absolute;font-size:17px;font-weight:500;line-height:22px;color:var(--white)}
.btn-outline{position:absolute;left:377px;top:596px;width:181px;height:38px;border:2px solid var(--white);border-radius:6px;color:var(--white);font-size:20px;font-weight:500;text-align:center;line-height:34px}

/* news */
.news{left:133px;width:855px;height:175px}
.news .thumb{position:absolute;left:0;top:0;width:141px;height:175px}
.news h3{position:absolute;left:159px;top:-4px;font-size:21px;font-weight:500;line-height:30px;color:var(--ink)}
.news p{position:absolute;left:159px;top:63px;width:696px;font-size:13px;line-height:22px;color:var(--grey);font-weight:300}
.news .more{position:absolute;left:754px;top:149px;width:101px;height:25px;background:var(--blue);border-radius:3px;color:var(--white);font-size:11.5px;font-weight:500;text-align:center;line-height:25px}
.tile{top:2480px;width:220px;height:247px;overflow:hidden}
.tile .cap{position:absolute;left:0;bottom:0;width:100%;height:86px;background:rgba(40,60,90,.55);padding:16px 0 0 18px;font-size:16.5px;line-height:29px;color:var(--white)}
.tile .cap.u{text-decoration:underline}

/* footer */
.footer{left:0;top:2787px;width:1200px;height:373px;background:linear-gradient(150deg,#0a4fa9,#0b55b3)}
.fline{left:110px;width:980px;height:1px;background:rgba(255,255,255,.3)}
.social{top:2822px;width:18px;height:18px;border-radius:50%;border:2px solid var(--blue-pale)}
.f-brand{left:164px;top:2888px;font-size:22px;font-weight:700;line-height:22px;color:var(--white);letter-spacing:.5px}
.f-addr{left:183px;font-size:12.5px;line-height:22px;color:var(--blue-pale)}
.f-addr b{color:var(--white);font-weight:500}
.f-col h4{position:absolute;font-size:19px;font-weight:500;color:var(--blue-pale)}
.f-col a{position:absolute;font-size:13px;color:var(--blue-light);text-decoration:none}
.copy{left:0;top:3118px;width:1200px;text-align:center;font-size:12.5px;color:var(--blue-light)}
</style>
</head>
<body>

<div class="abs topbar">
  <svg class="abs search" width="30" height="30" viewBox="0 0 30 30" aria-label="Search"><circle cx="12" cy="12" r="9" fill="none" stroke="#cadeef" stroke-width="2"/><line x1="19" y1="19" x2="28" y2="28" stroke="#cadeef" stroke-width="2.4"/></svg>
  <svg class="abs flag" style="left:895px" viewBox="0 0 44 25" aria-label="English">
    <rect width="44" height="25" fill="#fff"/>
    <g fill="#c8202f"><rect y="0" width="44" height="2"/><rect y="4" width="44" height="2"/><rect y="8" width="44" height="2"/><rect y="12" width="44" height="2"/><rect y="16" width="44" height="2"/><rect y="20" width="44" height="2"/><rect y="24" width="44" height="1"/></g>
    <rect width="19" height="13" fill="#2b3a7a"/>
  </svg>
  <svg class="abs flag" style="left:959px" viewBox="0 0 44 25" aria-label="Japanese"><rect width="44" height="25" fill="#fff"/><circle cx="22" cy="12.5" r="7" fill="#d3121d"/></svg>
  <svg class="abs flag" style="left:1024px" viewBox="0 0 44 25" aria-label="Chinese"><rect width="44" height="25" fill="#de2a1f"/><polygon points="7,3 8.4,7 12.5,7 9.2,9.4 10.4,13.4 7,11 3.6,13.4 4.8,9.4 1.5,7 5.6,7" fill="#ffde00"/></svg>
</div>

<div class="abs header"></div>
<div class="abs brand"><div class="brand-mark"></div><div class="brand-name">KORV LLP</div></div>
<nav class="nav">
  <a class="active" style="left:533px">HOME</a>
  <a style="left:600px">SERVICES</a>
  <a style="left:696px">TECHNOLOGIES</a>
  <a style="left:837px">PROFESSIONALS</a>
  <a style="left:987px">ABOUT US</a>
</nav>

<section class="abs hero"></section>
<h1 class="abs hero-title">PATENT<br>TRADEMARK<br>DESIGN<br>COPYRIGHT</h1>
<p class="abs hero-sub">Serving Clients, Fortune 500 And Individual Inventors, Since 2003.</p>
<div class="abs badge" role="img" aria-label="Gold laurel wreath with stars celebrating 20 years">
  <div class="abs badge-num">20</div>
  <div class="abs badge-txt">YEARS</div>
</div>

<div class="abs stats">
  <div class="stat" style="width:184px"><b>18K</b><span>Total Patents</span></div>
  <div class="stat" style="width:203px"><b>1.5K</b><span>Clients</span></div>
  <div class="stat" style="width:202px"><b>20</b><span>Years In Services</span></div>
  <div class="stat" style="width:187px"><b>450</b><span>Excellent Review</span></div>
</div>

<h2 class="abs sec-title" style="top:822px;font-size:35px">Services</h2>
<p class="abs sec-sub" style="top:879px">KORV Offers A Comprehensive Portfolio Of Intellectual Property Services.<br>Our Services Include:</p>

<svg class="abs arrow" style="left:42px" width="28" height="50" viewBox="0 0 28 50"><polyline points="26,2 3,25 26,48" fill="none" stroke="#2f72c4" stroke-width="2.5"/></svg>
<svg class="abs arrow" style="left:1128px" width="28" height="50" viewBox="0 0 28 50"><polyline points="2,2 25,25 2,48" fill="none" stroke="#2f72c4" stroke-width="2.5"/></svg>

<div class="abs card" style="left:110px">
  <div class="ico"><svg width="28" height="28" viewBox="0 0 28 28"><path d="M22 4 L9 19 L7 23 L11 21 L24 6 Z" fill="none" stroke="#fff" stroke-width="2"/><line x1="5" y1="25" x2="10" y2="25" stroke="#fff" stroke-width="2"/></svg></div>
  <h3>DESIGNS</h3>
  <p>Lorem Ipsum Dolor Sit Amet,<br>Consectetur Adipiscing Elit.</p>
</div>
<div class="abs card" style="left:365px">
  <div class="ico"><svg width="30" height="28" viewBox="0 0 30 28"><circle cx="10" cy="9" r="5" fill="none" stroke="#fff" stroke-width="2"/><circle cx="21" cy="9" r="5" fill="none" stroke="#fff" stroke-width="2"/><path d="M2 24 Q10 13 18 24 Z M13 24 Q21 13 29 24" fill="none" stroke="#fff" stroke-width="2"/></svg></div>
  <h3 class="two">EXPERT WITNESS<br>AND CONSULTING</h3>
  <p>Aliquet Nam Viverra Quam<br>Lectus Grae Pretium Cursus.</p>
</div>
<div class="abs card" style="left:620px">
  <div class="ico"><svg width="30" height="28" viewBox="0 0 30 28"><path d="M3 12 Q15 2 27 12 M7 16 Q15 9 23 16 M11 20 Q15 16 19 20" fill="none" stroke="#fff" stroke-width="2"/><line x1="6" y1="25" x2="25" y2="4" stroke="#fff" stroke-width="2"/></svg></div>
  <h3>INTERFERENCES</h3>
  <p>Ultrices Adipiscing Metus At<br>Vel Cras Torto Rhoncus Tellus</p>
</div>
<div class="abs card" style="left:875px">
  <div class="ico"><svg width="28" height="28" viewBox="0 0 28 28"><circle cx="14" cy="14" r="10" fill="none" stroke="#fff" stroke-width="2.5"/><circle cx="14" cy="14" r="4.5" fill="#fff"/></svg></div>
  <h3>ITC LITIGATION</h3>
  <p>Pretium Cursus. Urna Sem<br>Tincidunt Pretium &nbsp;Varius Id.</p>
</div>

<section class="abs tech">
  <h2>Technologies</h2>
  <p class="lead">KORV Attorneys Have Backgrounds In Every Technical Field, Including:</p>
  <div class="tlabel" style="left:48px;top:158px">Chemical Engineering<br>And Material Science</div>
  <div class="tlabel" style="left:416px;top:172px">Life Science</div>
  <div class="tlabel" style="left:783px;top:180px">Optics</div>
  <div class="ring" style="left:21px;top:207px;width:204px;height:204px"><div class="photo" role="img" aria-label="Laboratory microscope and glassware" style="width:168px;height:168px;background:radial-gradient(circle at 55% 45%,#d7e4f2,#6c8fb8 55%,#1d3f6e)"></div></div>
  <div class="ring" style="left:194px;top:283px;width:226px;height:226px"><div class="photo" role="img" aria-label="Electrical panel with wiring and breakers" style="width:186px;height:186px;background:radial-gradient(circle at 50% 45%,#e7e7e2,#8a8a80 55%,#2d2d2a)"></div></div>
  <div class="ring" style="left:376px;top:201px;width:180px;height:180px"><div class="photo" role="img" aria-label="Scientist working at a microscope" style="width:148px;height:148px;background:radial-gradient(circle at 50% 50%,#c5d6e8,#5d7fa6 55%,#1f3a5f)"></div></div>
  <div class="ring" style="left:523px;top:276px;width:226px;height:226px"><div class="photo" role="img" aria-label="Hand reaching toward metal gear assembly" style="width:186px;height:186px;background:radial-gradient(circle at 45% 45%,#f1ddd0,#a89283 55%,#3d3935)"></div></div>
  <div class="ring" style="left:715px;top:208px;width:180px;height:180px"><div class="photo" role="img" aria-label="Glowing fibre optic cable" style="width:148px;height:148px;background:radial-gradient(circle at 55% 50%,#e8f4ff,#3d86d6 45%,#0b1f4a)"></div></div>
  <div class="tlabel" style="left:157px;top:522px">Electrical Engineering And Software</div>
  <div class="tlabel" style="left:551px;top:511px">Mechanical Engineering</div>
  <div class="btn-outline">Learn More</div>
</section>

<h2 class="abs sec-title" style="top:1963px;font-size:35px">News And Publications</h2>

<article class="abs news" style="top:2067px">
  <div class="thumb" role="img" aria-label="Colourful fibre optic strands" style="background:linear-gradient(135deg,#3a6fd8,#b4c8f0 40%,#d85a9a 70%,#c9302c)"></div>
  <h3>Lorem Ipsum Dolor Sit Amet,<br>Consectetur ....</h3>
  <p>Lorem Ipsum Dolor Sit Amet, Consectetur Adipiscing Elit. Aliquet Ipsum Rhoncus Tortor In Nisi, Blandit Semper. Tellus At Nunc. Lorem Ipsum Dolor Sit Amet, Consectetur Adipiscing Elit. Aliquet Ipsum Rhoncus Tortor In Nisi, Blandit Semper. Tellus At Nunc.</p>
  <div class="more">Read More</div>
</article>
<article class="abs news" style="top:2273px">
  <div class="thumb" role="img" aria-label="Stack of steel gears" style="background:linear-gradient(135deg,#d8d8d8,#8c8c8c 50%,#4a4a4a)"></div>
  <h3>Lorem Ipsum Dolor Sit Amet,<br>Consectetur ....</h3>
  <p>Lorem Ipsum Dolor Sit Amet, Consectetur Adipiscing Elit. Aliquet Ipsum Rhoncus Tortor In Nisi, Blandit Semper. Tellus At Nunc. Lorem Ipsum Dolor Sit Amet, Consectetur Adipiscing Elit. Aliquet Ipsum Rhoncus Tortor In Nisi, Blandit Semper. Tellus At Nunc.</p>
  <div class="more">Read More</div>
</article>

<div class="abs tile" style="left:133px" role="img" aria-label="Telecommunications tower against blue sky"><div style="width:100%;height:100%;background:linear-gradient(180deg,#0a4fd0,#3d86e6 70%,#7a8ea8)"></div><div class="cap u">Lorem Ipsum Dolor Sit<br>Amet, Consectetur ....</div></div>
<div class="abs tile" style="left:371px" role="img" aria-label="Business people walking through glass office"><div style="width:100%;height:100%;background:linear-gradient(180deg,#e9f1f4,#a9c6c8 55%,#56707a)"></div><div class="cap">Lorem Ipsum Dolor Sit<br>Amet, Consectetur ....</div></div>
<div class="abs tile" style="left:609px" role="img" aria-label="Laboratory flasks with coloured liquids"><div style="width:100%;height:100%;background:linear-gradient(135deg,#dfe6e8,#7fb89a 45%,#b44a8c 75%,#5a4a8a)"></div><div class="cap">Lorem Ipsum Dolor Sit<br>Amet, Consectetur ....</div></div>
<div class="abs tile" style="left:847px" role="img" aria-label="Glowing circuit board with energy symbol"><div style="width:100%;height:100%;background:radial-gradient(circle at 55% 40%,#6fd0ff,#1a5cc0 40%,#0a1d4a)"></div><div class="cap">Lorem Ipsum Dolor Sit<br>Amet, Consectetur ....</div></div>

<footer class="abs footer"></footer>
<div class="abs social" style="left:944px" aria-label="Social link"></div>
<div class="abs social" style="left:985px" aria-label="Social link"></div>
<div class="abs social" style="left:1026px" aria-label="Social link"></div>
<div class="abs social" style="left:1067px" aria-label="Social link"></div>
<div class="abs fline" style="top:2868px"></div>

<div class="abs f-brand">KORV<br>LLP</div>
<svg class="abs" style="left:145px;top:2940px" width="30" height="40" viewBox="0 0 30 40" aria-label="Address"><path d="M15 2 C7 2 2 8 2 15 C2 25 15 38 15 38 C15 38 28 25 28 15 C28 8 23 2 15 2 Z" fill="#fff"/><circle cx="15" cy="15" r="5" fill="#0a50ae"/></svg>
<div class="abs f-addr" style="top:2940px"><b>Main Office</b><br>1200 Meridian Avenue<br>Suite 400<br>Fairview, VA &nbsp;22000</div>
<svg class="abs" style="left:147px;top:3046px" width="26" height="28" viewBox="0 0 26 28" aria-label="Phone"><path d="M5 2 L10 2 L12 8 L9 11 Q12 17 17 19 L20 16 L25 18 L25 23 Q24 26 20 26 Q4 22 2 6 Q2 2 5 2 Z" fill="none" stroke="#fff" stroke-width="1.8"/></svg>
<div class="abs f-addr" style="top:3048px">Tel: 555-014-2200<br>Fax: 555-014-2201</div>

<div class="f-col">
  <h4 style="left:433px;top:2891px">Quick Links</h4>
  <a style="left:433px;top:2943px">Services</a>
  <a style="left:433px;top:2974px">Technologies</a>
  <a style="left:433px;top:3005px">Professionals</a>
  <a style="left:433px;top:3036px">CAFC Alerts</a>

  <h4 style="left:682px;top:2891px">About</h4>
  <a style="left:682px;top:2943px">Offices</a>
  <a style="left:682px;top:2974px">Careers</a>
  <a style="left:682px;top:3005px">Firm History</a>
  <a style="left:682px;top:3036px">Contacts</a>
  <a style="left:682px;top:3067px">News And Publications</a>

  <h4 style="left:961px;top:2891px">Resources</h4>
  <a style="left:961px;top:2943px">Forms</a>
  <a style="left:961px;top:2974px">Materials</a>
  <a style="left:961px;top:3005px">News And Events</a>
  <a style="left:961px;top:3036px">Locations</a>
</div>

<div class="abs fline" style="top:3105px"></div>
<div class="abs copy">Copyright©Test. All Right Reserved</div>

</body>
</html>
```